Electronic Repair Company need a new flyer!

Hi Guys,

I need a new flyer for my repair company that I can use for my door 2 door marketing. The flyers will be send to thousands of addresses in the Netherlands. You can design the flyer in English but I need to be able to translate the flyer into Dutch, so I might need the PSD file.

We repair Computers, Laptops and ALL Velmora devices.

For some inspiration please take a look at: www.qorvatek.nl

And see the pictures below ;)

Target Market(s)

Computer & Smartphone Repair

Industry/Entity Type

Electronic

Requirements
Nice to have
• I would like to have some pictures from our staff (like on our website) in it so people can see who we really are :)

```html
<!DOCTYPE html>
<html lang="en">
<head>
<meta charset="utf-8">
<title>Qorvatek repair flyer</title>
<link rel="stylesheet" href="https://fonts.googleapis.com/css2?family=Open+Sans:wght@400;600;700;800&display=swap">
<style>
:root{
  --red:#e8452c;
  --red-soft:#ee6b52;
  --ink:#222;
  --grey-dark:#4a4a4a;
  --paper:#f0f0f0;
  --white:#fff;
  --page:#e6e6e6;
  --muted:#555;
}
*{box-sizing:border-box;margin:0;padding:0}
html,body{width:1020px;height:1200px;overflow:hidden;background:var(--page);font-family:"Open Sans",sans-serif;color:var(--ink)}
.flyer{position:absolute;left:84px;top:0;width:650px;height:915px;background:var(--paper);transform:scale(1.3115);transform-origin:0 0;overflow:hidden}
.abs{position:absolute}
.brand{left:28px;top:26px;display:flex;align-items:center;gap:8px;font-weight:800;font-size:30px;color:var(--ink);letter-spacing:.5px}
.brand-mark{width:22px;height:22px;background:var(--red)}
.site{right:22px;top:34px;display:flex;align-items:center;gap:8px;font-size:17px;color:var(--ink)}
.site svg{width:17px;height:17px}
.headline{right:22px;top:86px;text-align:right;color:var(--red);line-height:1.2}
.headline .thin{font-size:32px;font-weight:400;letter-spacing:.3px}
.headline .bold{font-size:25px;font-weight:700}
.staff-photo{left:40px;top:70px;width:320px;height:300px;background:radial-gradient(ellipse at 55% 45%,#d9a98a 0%,#e58a4a 28%,#cfcfcf 55%,var(--paper) 78%)}
.bands{left:0;top:0;width:650px;height:915px}
.slogan{right:22px;top:282px;text-align:right;color:var(--white);line-height:1.05}
.slogan .we{font-size:48px;font-weight:700}
.slogan .repair{font-size:32px;font-weight:700}
.slogan .social{font-size:26px;font-weight:400;margin-top:4px}
.slogan .life{font-size:54px;font-weight:400}
.offer{left:28px;top:368px;color:var(--red);line-height:1.15}
.offer .big{font-size:30px;font-weight:700}
.offer .small{font-size:19px;font-weight:400}
.cta{left:28px;top:487px;width:227px;height:43px;background:var(--red);color:var(--white);font-size:24px;font-weight:700;display:flex;align-items:center;padding-left:24px;box-shadow:0 4px 6px rgba(0,0,0,.3)}
.services{left:22px;top:553px;width:620px;display:flex;justify-content:space-between}
.service{width:120px}
.hex{width:42px;height:46px;margin:0 0 6px 26px}
.service h3{font-size:12px;font-weight:700;color:var(--ink);white-space:nowrap}
.service h3 span{color:var(--red)}
.ticks{list-style:none;margin-top:6px}
.ticks li{position:relative;font-size:10.5px;line-height:15px;padding-left:17px;color:#333;white-space:nowrap}
.ticks li::before{content:"";position:absolute;left:3px;top:2px;width:4px;height:8px;border:solid var(--red);border-width:0 2px 2px 0;transform:rotate(40deg)}
.hours{left:27px;top:708px;width:188px;height:140px;background:var(--red);border-radius:3px;overflow:hidden;box-shadow:0 2px 4px rgba(0,0,0,.25)}
.hours h4{background:var(--grey-dark);color:var(--white);font-weight:400;font-size:19px;padding:3px 14px;height:32px}
.hours .row{color:var(--white);font-size:13px;padding:2px 14px;line-height:17px;height:36px}
.hours .row b{display:block;font-weight:700}
.hours .row.alt{background:var(--red-soft)}
.genuine{left:233px;top:708px}
.genuine h4{font-size:17px;font-weight:700;color:var(--ink);line-height:20px}
.genuine p{font-size:15px;color:var(--red);line-height:18px}
.genuine .ticks{margin-top:6px}
.genuine .ticks li{line-height:13.5px;font-size:10px}
.makers{left:430px;top:712px;width:215px;display:grid;grid-template-columns:repeat(3,1fr);row-gap:30px;font-size:12px;font-weight:700;color:var(--muted);text-align:center}
.makers span{height:20px;line-height:20px}
.contact{left:32px;top:864px;font-size:10.5px;color:#333;display:flex;gap:16px}
.contact span,.social{display:flex;align-items:center;gap:5px}
.contact svg{width:10px;height:13px}
.social{left:32px;top:885px;font-size:10.5px;color:#333}
.social i{width:11px;height:11px;border-radius:50%;background:var(--red);display:inline-block}
.phone{left:425px;top:860px;width:225px;height:55px;background:var(--red);clip-path:polygon(18px 0,100% 0,100% 100%,0 100%);display:flex;align-items:center;gap:10px;padding-left:32px;color:var(--white);font-size:20px}
.phone svg{width:24px;height:24px}
</style>
</head>
<body>
<main class="flyer">
  <div class="staff-photo abs" role="img" aria-label="Smiling technician in a white and orange polo holding an open laptop and a charger cable"></div>

  <svg class="bands abs" viewBox="0 0 650 915" aria-hidden="true">
    <polygon points="648,160 325,415 648,538" fill="var(--red)"/>
    <polygon points="0,245 648,535 648,550 0,260" fill="var(--white)"/>
    <polygon points="0,260 648,550 648,580 0,274" fill="var(--grey-dark)"/>
  </svg>

  <div class="brand abs"><span class="brand-mark"></span>QORVATEK.NL</div>
  <div class="site abs">
    <svg viewBox="0 0 20 20"><circle cx="10" cy="10" r="8.5" fill="none" stroke="var(--red)" stroke-width="2"/><path d="M1.5 10h17M10 1.5c-4 4-4 13 0 17M10 1.5c4 4 4 13 0 17" fill="none" stroke="var(--red)" stroke-width="1.5"/></svg>
    www.qorvatek.nl
  </div>

  <div class="headline abs">
    <div class="thin">FAST, QUALITY AND</div>
    <div class="bold">ON NO CURE NO PAY!</div>
  </div>

  <div class="slogan abs">
    <div class="we">We</div>
    <div class="repair">repair your</div>
    <div class="social">social and business</div>
    <div class="life">life!</div>
  </div>

  <div class="offer abs">
    <div class="big">We repair</div>
    <div class="small">Computers Laptops and</div>
    <div class="big">ALL Velmora devices</div>
  </div>

  <div class="cta abs">OUR SERVICE</div>

  <section class="services abs">
    <div class="service">
      <svg class="hex" viewBox="0 0 42 46"><polygon points="21,2 39,12 39,34 21,44 3,34 3,12" fill="var(--white)" stroke="var(--red)" stroke-width="2"/><circle cx="21" cy="23" r="7" fill="var(--ink)"/></svg>
      <h3>VELMORA <span>REPAIR</span></h3>
      <ul class="ticks"><li>VelBook reparatie</li><li>VelDesk reparatie</li><li>VelPhone reparatie</li><li>VelPad reparatie</li></ul>
    </div>
    <div class="service">
      <svg class="hex" viewBox="0 0 42 46"><polygon points="21,2 39,12 39,34 21,44 3,34 3,12" fill="var(--white)" stroke="var(--red)" stroke-width="2"/><rect x="12" y="15" width="18" height="12" fill="var(--ink)"/><rect x="18" y="27" width="6" height="3" fill="var(--ink)"/><rect x="15" y="30" width="12" height="1.5" fill="var(--ink)"/></svg>
      <h3>COMPUTER <span>REPAIR</span></h3>
      <ul class="ticks"><li>Harlon reparatie</li><li>Dorvix reparatie</li><li>Medrix reparatie</li><li>Arcel reparatie</li></ul>
    </div>
    <div class="service">
      <svg class="hex" viewBox="0 0 42 46"><polygon points="21,2 39,12 39,34 21,44 3,34 3,12" fill="var(--white)" stroke="var(--red)" stroke-width="2"/><rect x="13" y="16" width="16" height="10" fill="none" stroke="var(--ink)" stroke-width="1.5"/><rect x="10" y="27" width="22" height="2.5" fill="var(--ink)"/></svg>
      <h3>LAPTOP <span>REPAIR</span></h3>
      <ul class="ticks"><li>Arcel reparatie</li><li>Azuro reparatie</li><li>Harlon reparatie</li><li>Dorvix reparatie</li></ul>
    </div>
    <div class="service">
      <svg class="hex" viewBox="0 0 42 46"><polygon points="21,2 39,12 39,34 21,44 3,34 3,12" fill="var(--white)" stroke="var(--red)" stroke-width="2"/><rect x="14" y="14" width="14" height="18" rx="1.5" fill="var(--ink)"/></svg>
      <h3>TABLET <span>REPAIR</span></h3>
      <ul class="ticks"><li>VelPad reparatie</li><li>Stellar reparatie</li><li>Planar reparatie</li><li>Azuro reparatie</li></ul>
    </div>
    <div class="service">
      <svg class="hex" viewBox="0 0 42 46"><polygon points="21,2 39,12 39,34 21,44 3,34 3,12" fill="var(--white)" stroke="var(--red)" stroke-width="2"/><rect x="16" y="13" width="10" height="20" rx="1.5" fill="var(--ink)"/></svg>
      <h3>SMARTPHONE <span>REPAIR</span></h3>
      <ul class="ticks"><li>VelPhone reparatie</li><li>Sorensa reparatie</li><li>Kelto reparatie</li><li>Norvik reparatie</li></ul>
    </div>
  </section>

  <section class="hours abs">
    <h4>Opening Hours</h4>
    <div class="row"><b>Monday / Friday:</b>8:00 a.m. to 18:00 pm</div>
    <div class="row alt"><b>Saturday:</b>10:00 to 17:00 pm</div>
    <div class="row"><b>Saturday:</b>10:00 to 17:00 pm</div>
  </section>

  <section class="genuine abs">
    <h4>GENUINE SERVICE.</h4>
    <p>We do nothing else!</p>
    <ul class="ticks">
      <li>Repair within 24 hours</li>
      <li>Smartphones within 30 minutes</li>
      <li>12 month warranty</li>
      <li>Passing by without an appointment</li>
      <li>Free &amp; delivery</li>
      <li>No cure no pay!</li>
    </ul>
  </section>

  <div class="makers abs">
    <span>Velmora</span><span>Dorvix</span><span>Harlon</span>
    <span>Sovan</span><span>Arcel</span><span>Azuro</span>
    <span>Sorensa</span><span>Lumeo</span><span>Fuseri</span>
  </div>

  <div class="contact abs">
    <span><svg viewBox="0 0 10 13"><path d="M5 0a4.5 4.5 0 0 0-4.5 4.5C.5 8 5 13 5 13s4.5-5 4.5-8.5A4.5 4.5 0 0 0 5 0z" fill="var(--red)"/><circle cx="5" cy="4.5" r="1.7" fill="var(--paper)"/></svg>Lindelaan 58, 1043 Amsterdam</span>
    <span><svg viewBox="0 0 10 13"><path d="M5 0a4.5 4.5 0 0 0-4.5 4.5C.5 8 5 13 5 13s4.5-5 4.5-8.5A4.5 4.5 0 0 0 5 0z" fill="var(--red)"/><circle cx="5" cy="4.5" r="1.7" fill="var(--paper)"/></svg>Korenweg 12, 2151 KM Nieuw-Vennep</span>
  </div>
  <div class="social abs"><i></i>social.qorvatek.nl/nederland</div>

  <div class="phone abs">
    <svg viewBox="0 0 24 24"><path d="M6.6 10.8a15 15 0 0 0 6.6 6.6l2.2-2.2c.3-.3.7-.4 1-.2 1.1.4 2.3.6 3.6.6.6 0 1 .4 1 1V20c0 .6-.4 1-1 1A17 17 0 0 1 3 4c0-.6.4-1 1-1h3.5c.6 0 1 .4 1 1 0 1.3.2 2.5.6 3.6.1.3 0 .7-.2 1z" fill="var(--white)"/></svg>
    088 417 26 30
  </div>
</main>
</body>
</html>
```